Keystone Ridge Construction LLC

We need a professional and colorful website that describes our company [please see below]:

CORE COMPETENCIES

About Us: Keystone Ridge Construction, LLC is a veteran-owned business, and is a leading force in the construction industry. We have continuously provided exceptional services to our clients. With a wealth of experience and a commitment of excellence, we have earned a reputation for delivering high-quality projects on time and within budget.

Core Competencies:

Experience: With decades of experience, we bring unparalleled expertise to every project we undertake. Our team consists of seasoned professionals who are experts in their respective fields.

Portfolio: Our portfolio encompasses a wide range of construction projects, including commercial building, industrial facilities, infrastructure development and more.

Innovation: We stay at the forefront of industry trends and technologies, leveraging the latest tools and techniques to deliver innovative solutions.

Client Satisfaction: Our commitment to client satisfaction is unwavering. We prioritize open communication, transparency, and responsiveness, working closely with clients to understand their needs and deliver results.

Safety: Safety is our top priority on every job site. We adhere to the highest safety standards and implement rigorous safety protocols to ensure the well-being of our workers and stakeholders.

KEY SERVICES

General Contracting
Construction Management
Design-Build Services
Pre-construction Planning
Value Engineering
Sustainable Construction Practices
Renovation and Remodeling
Quality Assurance and Control
Project Estimating and Budgeting
Permitting and Regulatory Compliance

CONTACT INFORMATION

Douglas Whitfield, President
Email Address [TBD]
Website Address [TBD]
555.214.6093

Federal Government and Commercial Agencies

Construction and Design Build

• Please use our attached logo and color scheme that was designed through Pixel Forum. Please include the Nation's Capitol building with a patriotic feel and include a diverse work force. Include federal buildings in the pictures. Please include in the opeing tagline that the company is Veteran Owned.

```html
<!DOCTYPE html>
<html lang="en">
<head>
<meta charset="utf-8">
<title>Keystone Ridge Construction</title>
<link rel="stylesheet" href="https://fonts.googleapis.com/css2?family=Cinzel:wght@600;700&family=Roboto:wght@400;500&family=Poppins:wght@400;600&display=swap">
<style>
:root{
  --navy:#2b3a80;
  --navy-deep:#243270;
  --green:#8cc63f;
  --ink:#222;
  --muted:#555;
  --foot:#141414;
  --white:#fff;
}
*{margin:0;padding:0;box-sizing:border-box}
html,body{width:1200px;height:2863px;overflow:hidden}
body{font-family:"Roboto",sans-serif;color:var(--ink);position:relative;background:#fff}
.abs{position:absolute}
.btn{position:absolute;display:flex;align-items:center;gap:8px;background:var(--green);color:#fff;font:500 15px "Roboto",sans-serif;padding:0 36px 0 16px;height:48px;clip-path:polygon(0 0,86% 0,100% 100%,0 100%)}
.btn svg{width:16px;height:10px}

/* header */
.site-header{left:0;top:0;width:1200px;height:108px;background:linear-gradient(90deg,var(--navy) 0%,#4d6a8a 45%,var(--green) 100%)}
.brand{left:111px;top:36px;color:#fff;font:700 24px "Cinzel",serif;letter-spacing:1px;display:flex;align-items:center;gap:10px}
.brand i{width:14px;height:14px;background:var(--green);display:block}
.nav{left:397px;top:44px;display:flex;gap:23px;color:#fff;font-size:15px}
.nav .active{text-decoration:underline}
.nav-divider{left:954px;top:36px;width:1px;height:36px;background:rgba(255,255,255,.6)}
.phone{left:978px;top:43px;color:#fff;font:500 16px "Roboto",sans-serif;display:flex;gap:10px;align-items:center}

/* hero */
.hero{left:0;top:108px;width:1200px;height:584px;background:linear-gradient(180deg,#3a5598 0%,#6f8fc0 45%,#c9cfd6 70%,#e4e4e2 100%)}
.hero-title{left:111px;top:170px;font:700 58px/70px "Cinzel",serif;color:#fff}
.hero-title .accent{color:var(--green)}
.hero-text{left:111px;top:392px;width:340px;color:#fff;font-size:15px;line-height:26px}

/* about */
.about-deco{left:10px;top:742px;width:210px;height:570px;background:linear-gradient(90deg,#f3f7ea,#f0f1f5);clip-path:polygon(0 0,20% 6%,20% 100%,0 100%,0 0,30% 30%,30% 30%)}
.h2{font:700 40px "Cinzel",serif;color:var(--navy)}
.h2 .accent{color:var(--green)}
.rule{display:inline-block;width:64px;height:2px;background:var(--green);vertical-align:middle;margin-left:10px}
.about-title{left:111px;top:845px}
.about-text{left:111px;top:925px;width:411px;font-size:15px;line-height:27.5px;text-align:justify;color:#333}
.about-frame{left:604px;top:755px;width:472px;height:462px;border:1.5px solid var(--green);clip-path:polygon(0 9%,100% 0,100% 100%,0 100%)}
.about-photo{left:616px;top:765px;width:473px;height:465px;background:linear-gradient(135deg,#c7c7c0,#9e9e96 55%,#3c5f94);clip-path:polygon(0 12%,100% 0,100% 100%,0 100%)}

/* core */
.core{left:0;top:1315px;width:1200px;height:600px;background:linear-gradient(90deg,var(--navy-deep),#33448a 60%,#2e3f82)}
.core-title{left:111px;top:1400px;color:#fff;font-size:38px;line-height:52px}
.core-list{left:606px;top:1398px;width:464px;color:#fff}
.core-item{position:relative;padding-left:38px;margin-bottom:14px}
.core-item svg{position:absolute;left:0;top:2px}
.core-item h3{font:500 17.5px "Roboto",sans-serif;margin-bottom:4px}
.core-item p{font-size:11.5px;line-height:19px;color:#d6dbec;text-align:justify}
.dots{background-image:radial-gradient(var(--green) 1.4px,transparent 1.6px);background-size:16.7px 16.7px}

/* services */
.services-title{left:0;top:1985px;width:1200px;text-align:center}
.card{position:absolute;top:2077px;width:228px;height:320px;background:#fff;box-shadow:0 4px 14px rgba(0,0,0,.08)}
.card .photo{height:185px;clip-path:polygon(0 0,100% 0,100% 100%,0 94%)}
.card h3{font:500 18.5px "Roboto",sans-serif;color:#333;margin:34px 20px 0}
.card .btn{left:20px;top:256px;height:42px;font-size:13px;padding-right:32px}
.card.featured{background:var(--navy)}
.card.featured h3{color:#fff;margin-top:14px;line-height:27px}
.arrow{position:absolute;width:46px;height:46px;border-radius:50%;display:flex;align-items:center;justify-content:center}

/* footer */
.footer{left:0;top:2503px;width:1200px;height:360px;background:var(--foot);color:#ddd}
.foot-brand{left:111px;top:2650px;color:#fff;font:700 30px "Cinzel",serif;display:flex;gap:12px;align-items:center}
.foot-brand i{width:16px;height:16px;background:var(--green);display:block}
.foot-divider{left:390px;top:2572px;width:1px;height:175px;background:#333}
.foot-col{top:2568px;font-size:15px;color:#ddd}
.foot-col h4{font:600 19px "Poppins",sans-serif;color:#fff;margin-bottom:12px}
.foot-col li{list-style:none;line-height:26px;display:flex;gap:12px;align-items:center}
.foot-col li span{color:#bbb;font-size:11px}
.contact li{align-items:flex-start;margin-bottom:14px;line-height:25px}
.foot-rule{left:111px;top:2775px;width:978px;height:1px;background:#2c2c2c}
.socials{left:111px;top:2798px;display:flex;gap:8px}
.socials span{width:36px;height:36px;border-radius:50%;background:#fff;display:block}
.socials span:first-child{background:var(--green)}
.copyright{left:560px;top:2808px;color:#eee;font-size:15px}
</style>
</head>
<body>

<header class="abs site-header">
  <div class="abs brand"><i></i>KEYSTONE RIDGE</div>
  <nav class="abs nav">
    <span class="active">Home</span><span>About us</span><span>Core Competencies</span><span>Experience</span><span>Portfolio</span><span>More &#8964;</span>
  </nav>
  <div class="abs nav-divider"></div>
  <div class="abs phone">
    <svg width="18" height="18" viewBox="0 0 24 24" fill="#fff"><path d="M6.6 10.8c1.4 2.8 3.8 5.1 6.6 6.6l2.2-2.2c.3-.3.7-.4 1-.2 1.1.4 2.3.6 3.6.6.6 0 1 .4 1 1V20c0 .6-.4 1-1 1C10.6 21 3 13.4 3 4c0-.6.4-1 1-1h3.5c.6 0 1 .4 1 1 0 1.3.2 2.5.6 3.6.1.3 0 .7-.2 1l-2.3 2.2z"/></svg>
    +1 (555) 300 7742
  </div>
</header>

<section class="abs hero" role="img" aria-label="The Nation's Capitol building under a waving American flag sky"></section>
<h1 class="abs hero-title">Keystone<br><span class="accent">Ridge</span><br>Construction</h1>
<p class="abs hero-text">Keystone Ridge Construction, LLC [KRC LLC] is a veteran-owned business, and is a leading force in the construction industry.</p>
<a class="btn" style="left:111px;top:489px">Get Started <svg viewBox="0 0 16 10"><path d="M0 5h14M10 1l4 4-4 4" stroke="#fff" stroke-width="1.6" fill="none"/></svg></a>

<section aria-label="About us">
  <div class="abs" style="left:10px;top:742px;width:45px;height:570px;background:#f4f8ec;clip-path:polygon(0 0,100% 6%,100% 100%,0 100%)"></div>
  <div class="abs" style="left:80px;top:940px;width:68px;height:372px;background:#eef0f6;clip-path:polygon(0 0,100% 10%,100% 100%,0 100%)"></div>
  <div class="abs" style="left:172px;top:1112px;width:48px;height:200px;background:#f4f8ec;clip-path:polygon(0 0,100% 14%,100% 100%,0 100%)"></div>
  <h2 class="abs h2 about-title">About <span class="accent">Us</span><span class="rule"></span></h2>
  <p class="abs about-text">Keystone Ridge Construction, LLC [KRC LLC] is a veteran-owned business, and is a leading force in the construction industry. We have continuously provided exceptional services to our clients. With a wealth of experience and a commitment of excellence, we have earned a reputation for delivering high-quality projects on time and within budget.</p>
  <a class="btn" style="left:111px;top:1160px">Learn More <svg viewBox="0 0 16 10"><path d="M0 5h14M10 1l4 4-4 4" stroke="#fff" stroke-width="1.6" fill="none"/></svg></a>
  <div class="abs about-frame"></div>
  <div class="abs about-photo" role="img" aria-label="Close view of federal building columns with ornate capitals"></div>
  <div class="abs dots" style="left:1028px;top:1168px;width:110px;height:92px"></div>
</section>

<section class="abs core" role="img" aria-label="Federal courthouse facade in deep navy tint"></section>
<div class="abs dots" style="left:0;top:1575px;width:90px;height:92px"></div>
<h2 class="abs h2 core-title">Core<br>Competencies<span class="rule"></span></h2>
<div class="abs core-list">
  <div class="core-item"><svg width="22" height="18" viewBox="0 0 22 18"><path d="M2 9l6 6L20 2" stroke="#8cc63f" stroke-width="3.5" fill="none"/></svg><h3>Experience</h3><p>With decades of experience, we bring unparalleled expertise to every project we undertake. Our team consists of seasoned professionals who are experts in their respective fields.</p></div>
  <div class="core-item"><svg width="22" height="18" viewBox="0 0 22 18"><path d="M2 9l6 6L20 2" stroke="#8cc63f" stroke-width="3.5" fill="none"/></svg><h3>Portfolio</h3><p>Our portfolio encompasses a wide range of construction projects, including commercial building, industrial facilities, infrastructure development and more.</p></div>
  <div class="core-item"><svg width="22" height="18" viewBox="0 0 22 18"><path d="M2 9l6 6L20 2" stroke="#8cc63f" stroke-width="3.5" fill="none"/></svg><h3>Innovation</h3><p>We stay at the forefront of industry trends and technologies, leveraging the latest tools and techniques to deliver innovative solutions.</p></div>
  <div class="core-item"><svg width="22" height="18" viewBox="0 0 22 18"><path d="M2 9l6 6L20 2" stroke="#8cc63f" stroke-width="3.5" fill="none"/></svg><h3>Client Satisfaction</h3><p>Our commitment to client satisfaction is unwavering. We prioritize open communication, transparency, and responsiveness, working closely with clients to understand their needs and deliver results.</p></div>
  <div class="core-item"><svg width="22" height="18" viewBox="0 0 22 18"><path d="M2 9l6 6L20 2" stroke="#8cc63f" stroke-width="3.5" fill="none"/></svg><h3>Safety</h3><p>Safety is our top priority on every job site. We adhere to the highest safety standards and implement rigorous safety protocols to ensure the well-being of our workers and stakeholders.</p></div>
</div>

<h2 class="abs h2 services-title"><span class="rule" style="margin:0 18px 0 0"></span>Our <span class="accent">Services</span><span class="rule" style="margin-left:18px"></span></h2>
<div class="abs dots" style="left:78px;top:2340px;width:110px;height:80px"></div>
<div class="arrow" style="left:41px;top:2214px;border:2px solid var(--green)"><svg width="14" height="22" viewBox="0 0 14 22"><path d="M11 2L3 11l8 9" stroke="#8cc63f" stroke-width="2.4" fill="none"/></svg></div>
<div class="arrow" style="left:1105px;top:2214px;background:var(--green);width:44px;height:44px"><svg width="14" height="22" viewBox="0 0 14 22"><path d="M3 2l8 9-8 9" stroke="#fff" stroke-width="2.4" fill="none"/></svg></div>

<div class="card" style="left:111px"><div class="photo" role="img" aria-label="Contractor and client shaking hands" style="background:linear-gradient(135deg,#c98b62,#e9e2da)"></div><h3>General Contracting</h3><a class="btn">Learn More <svg viewBox="0 0 16 10"><path d="M0 5h14M10 1l4 4-4 4" stroke="#fff" stroke-width="1.6" fill="none"/></svg></a></div>
<div class="card featured" style="left:361px"><div class="photo" role="img" aria-label="Construction manager in hard hat reviewing plans on site" style="background:linear-gradient(135deg,#6f9fd0,#c7b24a 70%,#e7d65a)"></div><h3>Construction<br>Management</h3><a class="btn">Learn More <svg viewBox="0 0 16 10"><path d="M0 5h14M10 1l4 4-4 4" stroke="#fff" stroke-width="1.6" fill="none"/></svg></a></div>
<div class="card" style="left:611px"><div class="photo" role="img" aria-label="Building under construction wrapped in scaffolding" style="background:linear-gradient(180deg,#d8dde3,#8c7a6e)"></div><h3>Design-Build Services</h3><a class="btn">Learn More <svg viewBox="0 0 16 10"><path d="M0 5h14M10 1l4 4-4 4" stroke="#fff" stroke-width="1.6" fill="none"/></svg></a></div>
<div class="card" style="left:861px"><div class="photo" role="img" aria-label="Domed government building under restoration" style="background:linear-gradient(180deg,#bccbdc,#b08467 70%,#c9533a)"></div><h3>Value Engineering</h3><a class="btn">Learn More <svg viewBox="0 0 16 10"><path d="M0 5h14M10 1l4 4-4 4" stroke="#fff" stroke-width="1.6" fill="none"/></svg></a></div>

<div class="abs" style="left:1154px;top:2457px;width:46px;height:44px;border-radius:50%;background:var(--navy);display:flex;align-items:center;justify-content:center;gap:4px"><i style="width:6px;height:6px;background:#fff;border-radius:50%"></i><i style="width:6px;height:6px;background:#fff;border-radius:50%"></i><i style="width:6px;height:6px;background:#fff;border-radius:50%"></i></div>

<footer class="abs footer"></footer>
<div class="abs foot-brand"><i></i>KEYSTONE RIDGE</div>
<div class="abs foot-divider"></div>
<div class="abs foot-col" style="left:432px"><h4>Quick Links</h4><ul><li><span>&raquo;</span>Home</li><li><span>&raquo;</span>About us</li><li><span>&raquo;</span>Core Competencies</li><li><span>&raquo;</span>Services</li></ul></div>
<div class="abs foot-col" style="left:639px"><h4>Our Company</h4><ul><li><span>&raquo;</span>Terms &amp; Conditions</li><li><span>&raquo;</span>Privacy Policy</li><li><span>&raquo;</span>About Us</li><li><span>&raquo;</span>Support</li></ul></div>
<div class="abs foot-col contact" style="left:864px"><h4>Contact us</h4><ul>
  <li><svg width="14" height="18" viewBox="0 0 14 18" style="margin-top:4px"><path d="M7 0a7 7 0 0 0-7 7c0 5 7 11 7 11s7-6 7-11a7 7 0 0 0-7-7zm0 10a3 3 0 1 1 0-6 3 3 0 0 1 0 6z" fill="#fff"/></svg>Douglas Whitfield,<br>President</li>
  <li><svg width="16" height="16" viewBox="0 0 24 24" style="margin-top:4px"><path fill="#fff" d="M6.6 10.8c1.4 2.8 3.8 5.1 6.6 6.6l2.2-2.2c.3-.3.7-.4 1-.2 1.1.4 2.3.6 3.6.6.6 0 1 .4 1 1V20c0 .6-.4 1-1 1C10.6 21 3 13.4 3 4c0-.6.4-1 1-1h3.5c.6 0 1 .4 1 1 0 1.3.2 2.5.6 3.6.1.3 0 .7-.2 1l-2.3 2.2z"/></svg>555.214.6093</li>
  <li><svg width="16" height="13" viewBox="0 0 16 13" style="margin-top:7px"><path fill="#fff" d="M0 0h16v13H0z"/><path d="M0 0l8 6 8-6" stroke="#141414" stroke-width="1.4" fill="none"/></svg>info@keystoneridge.com</li>
</ul></div>
<div class="abs foot-rule"></div>
<div class="abs socials"><span></span><span></span><span></span><span></span></div>
<p class="abs copyright">&copy;Copyrights 2024 Keystone Ridge Construction &nbsp;| &nbsp;All Rights Reserved</p>

</body>
</html>
```